stationary for home builder
Birchwood Custom Homes, Inc.
Project: stationary for home builder
stationary for home builder - Real Estate
Creative Brief
Professional
Dale Morrow
President
4200 Tern Avenue, suite 310 Larkspur Bay, CA 90417
bchdalemorrow@mailvista.test

```html
<!DOCTYPE html>
<html lang="en">
<head>
<meta charset="utf-8">
<title>Birchwood Custom Homes – Business Cards</title>
<link href="https://fonts.googleapis.com/css2?family=Cinzel:wght@400;600&display=swap" rel="stylesheet">
<style>
  :root {
    --backdrop: #e6e7e8;
    --card: #ffffff;
    --brand-red: #b3241e;
    --brand-red-light: #d9443a;
    --steel: #8e9094;
    --steel-light: #c4c6c9;
    --ink: #4a4a4a;
  }
  * { box-sizing: border-box; margin: 0; padding: 0; }
  html, body { width: 1200px; height: 982px; overflow: hidden; }
  body {
    background: var(--backdrop);
    font-family: "Cinzel", "Times New Roman", serif;
    color: var(--ink);
    display: flex;
    flex-direction: column;
    align-items: center;
    justify-content: center;
    gap: 40px;
  }
  .card {
    position: relative;
    width: 760px;
    height: 434px;
    border-radius: 26px;
    overflow: hidden;
    background: var(--card);
    box-shadow: 0 4px 14px rgba(0,0,0,0.12);
  }
  .card-swoosh { position: absolute; inset: 0; width: 100%; height: 100%; }
  .card-content { position: absolute; inset: 0; }

  .wordmark {
    position: absolute;
    left: 0; right: 0;
    display: flex;
    align-items: center;
    justify-content: center;
    gap: 14px;
    color: var(--brand-red);
    font-size: 30px;
    font-weight: 600;
    letter-spacing: 0.04em;
  }
  .wordmark-square {
    width: 26px; height: 26px;
    background: var(--brand-red);
  }
  .card-front .wordmark { top: 192px; }
  .card-back .wordmark { top: 112px; }

  .contact-block {
    position: absolute;
    top: 200px; left: 0; right: 0;
    display: flex;
    justify-content: center;
  }
  .identity {
    text-align: right;
    padding-right: 18px;
    font-size: 15px;
    line-height: 1.5;
  }
  .identity .person-name { color: var(--brand-red); font-size: 19px; font-weight: 600; }
  .identity .person-title { font-size: 14px; margin-bottom: 4px; }
  .divider { width: 1px; background: var(--steel); }
  .channels {
    list-style: none;
    padding-left: 18px;
    font-size: 14px;
    line-height: 1.85;
  }
  .channels li { display: flex; align-items: center; gap: 8px; }
  .channel-icon { width: 16px; height: 16px; flex: none; }
</style>
</head>
<body>

  <article class="card card-front">
    <svg class="card-swoosh" viewBox="0 0 760 434" aria-hidden="true">
      <defs>
        <linearGradient id="redFront" x1="0" y1="0" x2="1" y2="1">
          <stop offset="0" stop-color="#8f1b16"/><stop offset="1" stop-color="#d9443a"/>
        </linearGradient>
        <linearGradient id="steelFront" x1="0" y1="0" x2="1" y2="1">
          <stop offset="0" stop-color="#6f7175"/><stop offset="1" stop-color="#c4c6c9"/>
        </linearGradient>
      </defs>
      <rect x="0" y="0" width="760" height="434" fill="url(#steelFront)"/>
      <ellipse cx="380" cy="217" rx="446" ry="280" fill="url(#redFront)"/>
      <ellipse cx="380" cy="217" rx="432" ry="267" fill="var(--steel-light)"/>
      <ellipse cx="380" cy="217" rx="426" ry="261" fill="var(--card)"/>
    </svg>
    <div class="card-content">
      <div class="wordmark"><span class="wordmark-square"></span>Birchwood Custom Homes, Inc.</div>
    </div>
  </article>

  <article class="card card-back">
    <svg class="card-swoosh" viewBox="0 0 760 434" aria-hidden="true">
      <defs>
        <linearGradient id="redBack" x1="0" y1="0" x2="1" y2="1">
          <stop offset="0" stop-color="#8f1b16"/><stop offset="1" stop-color="#d9443a"/>
        </linearGradient>
      </defs>
      <rect x="0" y="0" width="760" height="434" fill="url(#redBack)"/>
      <ellipse cx="380" cy="217" rx="432" ry="267" fill="var(--steel-light)"/>
      <ellipse cx="380" cy="217" rx="426" ry="261" fill="var(--card)"/>
    </svg>
    <div class="card-content">
      <div class="wordmark"><span class="wordmark-square"></span>Birchwood Custom Homes, Inc.</div>
      <div class="contact-block">
        <div class="identity">
          <div class="person-name">Dale Morrow</div>
          <div class="person-title">President</div>
          <div>4200 Tern Avenue, suite 310</div>
          <div>Larkspur Bay, CA 90417</div>
        </div>
        <div class="divider"></div>
        <ul class="channels">
          <li>
            <svg class="channel-icon" viewBox="0 0 16 16"><circle cx="8" cy="8" r="8" fill="var(--brand-red)"/><path d="M5 4.5l1.6-.5 1 2-1 .8a5 5 0 0 0 2.6 2.6l.8-1 2 1-.5 1.6c-3.4.2-6.6-3-6.5-6.5z" fill="#fff"/></svg>
            555-201-0142
          </li>
          <li>
            <svg class="channel-icon" viewBox="0 0 16 16"><circle cx="8" cy="8" r="8" fill="var(--brand-red)"/><rect x="5.5" y="3.5" width="5" height="9" rx="1" fill="#fff"/></svg>
            555-201-0187
          </li>
          <li>
            <svg class="channel-icon" viewBox="0 0 16 16"><circle cx="8" cy="8" r="8" fill="var(--brand-red)"/><rect x="4" y="5" width="8" height="6" fill="#fff"/><path d="M4 5l4 3 4-3" fill="none" stroke="var(--brand-red)" stroke-width="0.9"/></svg>
            bchdalemorrow@mailvista.test
          </li>
          <li>
            <svg class="channel-icon" viewBox="0 0 16 16"><circle cx="8" cy="8" r="8" fill="var(--brand-red)"/><circle cx="8" cy="8" r="4" fill="none" stroke="#fff" stroke-width="1"/><path d="M4 8h8M8 4c-2 2.5-2 5.5 0 8M8 4c2 2.5 2 5.5 0 8" fill="none" stroke="#fff" stroke-width="0.8"/></svg>
            www.birchwoodhomes.test
          </li>
        </ul>
      </div>
    </div>
  </article>

</body>
</html>
```